Internet plattform about horses with place for banners

We would like to redesign our website www.paddora.ch. We would like a simple, but modern & elegant design.
Of course the final design will be responive - but we'll start with the desktop design..

-> IMPORTANT: We will need place for 2 BANNERS: one 944x250 pixels and another 300x250px
-> We don't want any big image on the top - this takes too much place. (When we have no banners hired, we can put images of horses in place of the banners)
-> Background should be clear or white
-> Text on buttons should be text and no images
-> I would appreciate a smooth line somewhere that makes the whole design not too "rectangular"

A design we like is: www.brontavi.ch (but don't do exactly the same)
-> see possible disposal of elements for top of the page -> new design.gif

On the startpage the most important are the news, as well as a new classifieds, new events .. exact content is not that important for this contest as we will offer our users possibility of choosing which content they will like.

I just upload some images you could use, but it's not a must.
If you need images, you could also take some ones on http://lumofoto.varo.info/plonek/index.php (it's a friend of mine, so I would pay her the rights if we keep your project)

For this contest I don't expect different designs for mobile phones and don't need a css or anything else, just good ideas. Once we choose a partner this would be another job for you.

(Later, we'll work on the logo ...)

Target Market(s)

Swiss people who like horses and equestrian sports

Industry/Entity Type

Internet

Number of Pages Required

1 page

Font styles to use
Serif

Requirements
Must have
• Place for Maxiboard(944x250px) and halfpage(300x250) banners.
• The look should be modern, elegant and serious but not elitist. We should place banners for banks and other luxury sector, but all horse lovers should feel welcome. It should stay a popular site.
Nice to have
• A light element, a smooth or round line that makes the design not just rectangular...
• The design should leave much place for the information
• We leave the choice of colors open, but I like blue.. but will not be the only person to chose.
• You have the adress of our actual site (so feel free to open it - go on the contact page and send us a message,
Should not have
• no flashing design, no dark background, no big header.

```html
<!DOCTYPE html>
<html lang="en">
<head>
<meta charset="utf-8">
<title>Paddora – Die Schweizer Pferdeplatform</title>
<link href="https://fonts.googleapis.com/css2?family=Lato:wght@300;400;700&family=Dosis:wght@600&display=swap" rel="stylesheet">
<style>
  :root {
    --blue: #3b6de0;
    --blue-dark: #2f5cc7;
    --text: #2b2b2b;
    --muted: #555;
    --line: #cfcfcf;
    --section-bg: #f1f1f1;
    --caption: rgba(20, 20, 20, 0.6);
    --footer: #000;
    --white: #fff;
  }
  * { box-sizing: border-box; margin: 0; padding: 0; }
  html, body { width: 1200px; height: 994px; overflow: hidden; background: var(--white); }
  body { font-family: "Lato", sans-serif; color: var(--text); position: relative; }

  .site-header { position: absolute; top: 0; left: 0; width: 1200px; height: 146px; }
  .brand-mark {
    position: absolute; left: 161px; top: 11px; width: 125px; height: 125px;
    border: 1px solid var(--line); border-radius: 50%;
    display: flex; align-items: center; justify-content: center;
    font-size: 20px; font-weight: 700; color: var(--text);
  }
  .tagline { position: absolute; left: 318px; top: 48px; font-size: 19px; font-weight: 700; color: #333; line-height: 34px; }

  .header-tools { position: absolute; left: 803px; top: 38px; width: 236px; }
  .tool-row { display: flex; align-items: center; height: 18px; }
  .flag { width: 27px; height: 16px; display: flex; margin-right: 14px; }
  .flag span { flex: 1; }
  .flag.de { flex-direction: column; }
  .mail { display: flex; align-items: center; margin-left: 2px; font-size: 13px; color: #333; }
  .mail svg { margin-right: 6px; }
  .search { display: flex; margin-top: 21px; height: 30px; width: 235px; }
  .search input {
    flex: 1; border: 1px solid #bbb; border-right: 0; background: #f5f5f5;
    font: italic 12px "Lato", sans-serif; padding: 0 6px; color: #555;
  }
  .search button { width: 37px; border: 0; background: var(--blue); display: flex; align-items: center; justify-content: center; }

  .main-nav { position: absolute; top: 146px; left: 0; width: 1200px; height: 44px; background: var(--blue); }
  .main-nav ul { list-style: none; display: flex; justify-content: space-between; width: 878px; margin-left: 161px; height: 44px; align-items: center; }
  .main-nav li { font-family: "Dosis", sans-serif; font-weight: 600; font-size: 16px; color: #e4ebfb; position: relative; letter-spacing: 0.2px; }
  .main-nav li.active { color: var(--white); }
  .main-nav li.active::after {
    content: ""; position: absolute; left: 50%; bottom: -12px; margin-left: -6px;
    border: 6px solid transparent; border-bottom-color: var(--white);
  }

  .banner { position: absolute; top: 190px; height: 290px; overflow: hidden; }
  .banner-main { left: 0; width: 795px; border-radius: 0 0 6px 0;
    background: linear-gradient(100deg, #6a3419 0%, #9a4d22 35%, #c49b82 55%, #8ea377 80%, #5f7a45 100%); }
  .banner-side { left: 810px; width: 390px; border-radius: 0 0 0 6px;
    background: linear-gradient(100deg, #b58a55 0%, #4b5a52 45%, #b9433f 75%, #6e5a50 100%); }
  .banner-caption {
    position: absolute; left: 0; bottom: 0; width: 100%; height: 62px; background: var(--caption);
    color: var(--white); font-size: 24px; line-height: 62px;
  }
  .banner-main .banner-caption { padding-left: 162px; }
  .banner-side .banner-caption { padding-left: 24px; }
  .slide-arrow {
    position: absolute; top: 312px; width: 44px; height: 44px; border-radius: 50%;
    background: var(--blue); display: flex; align-items: center; justify-content: center;
  }
  .slide-arrow.prev { left: 23px; background: var(--blue-dark); }
  .slide-arrow.next { left: 728px; }

  .intro { position: absolute; top: 500px; left: 188px; width: 824px; text-align: center; font-size: 19px; line-height: 27px; color: #333; }

  .content-band { position: absolute; top: 570px; left: 0; width: 1200px; height: 380px; background: var(--section-bg); }
  .tiles { position: absolute; top: 5px; left: 161px; display: flex; gap: 10px; }
  .tile { position: relative; width: 168px; height: 167px; border-radius: 5px; overflow: hidden; }
  .tile-caption {
    position: absolute; left: 0; bottom: 0; width: 100%; height: 33px; background: var(--caption);
    color: var(--white); font-size: 17px; line-height: 33px; text-align: center;
  }
  .tile-caption::after { content: "›"; margin-left: 9px; }
  .t-news { background: linear-gradient(160deg, #3f6b2f, #8a8b86 55%, #4f6a3a); }
  .t-ads { background: linear-gradient(160deg, #4d6b3a, #c9cbc7 45%, #3a3a36); }
  .t-agenda { background: linear-gradient(160deg, #6b3818, #c98c3c 50%, #7a4a22); }
  .t-directory { background: linear-gradient(180deg, #4f7f36, #6a3a22 60%, #e9e9e9); }
  .t-forum { background: linear-gradient(160deg, #e8e8e8, #f6f6f6 50%, #cfcfcf); }

  .partners-title { position: absolute; top: 210px; width: 1200px; text-align: center; font-size: 24px; font-weight: 300; color: #222; }
  .partners { position: absolute; top: 268px; left: 161px; display: flex; gap: 12px; }
  .partner { width: 166px; height: 71px; border: 1px solid #cdcdcd; background: #f7f7f7; display: flex; align-items: center; justify-content: center; }
  .pb-1 { width: 144px; height: 36px; background: #1a1a1a; }
  .pb-2 { width: 148px; height: 46px; background: #d6e8d2; border-radius: 4px; }
  .pb-3 { width: 62px; height: 62px; background: #e0534f; }
  .pb-4 { width: 62px; height: 62px; background: #6c8b4f; }
  .pb-5 { width: 136px; height: 28px; background: #5c8fbd; }
  .partner-arrow {
    position: absolute; top: 293px; width: 22px; height: 22px; border-radius: 50%;
    background: #f5f5f5; border: 1px solid #bbb; display: flex; align-items: center; justify-content: center;
  }
  .partner-arrow.prev { left: 124px; }
  .partner-arrow.next { left: 1054px; }

  .site-footer { position: absolute; top: 950px; left: 0; width: 1200px; height: 44px; background: var(--footer);
    color: var(--white); font-size: 13px; text-align: center; line-height: 44px; letter-spacing: 0.3px; }
</style>
</head>
<body>
  <header class="site-header">
    <div class="brand-mark">Paddora.ch</div>
    <div class="tagline">
      <p>Die Schweizer Pferdeplatform</p>
      <p>La Plateforme Suisse Des Amis Du Cheval</p>
    </div>
    <div class="header-tools">
      <div class="tool-row">
        <div class="flag fr"><span style="background:#1c3f9c"></span><span style="background:#fff"></span><span style="background:#e0202a"></span></div>
        <div class="flag de"><span style="background:#000"></span><span style="background:#dd0000"></span><span style="background:#ffce00"></span></div>
        <div class="mail">
          <svg width="22" height="14" viewBox="0 0 22 14"><rect x="0.5" y="0.5" width="21" height="13" fill="#3b6de0" stroke="#2f5cc7"/><path d="M1 1 L11 8 L21 1 M1 13 L8 6 M21 13 L14 6" stroke="#fff" stroke-width="1.2" fill="none"/></svg>
          info@paddora.ch
        </div>
      </div>
      <form class="search">
        <input type="text" placeholder="Search...">
        <button type="button" aria-label="Search">
          <svg width="16" height="16" viewBox="0 0 16 16"><circle cx="7" cy="7" r="5.5" stroke="#fff" stroke-width="1.6" fill="none"/><path d="M11 11 L15 15" stroke="#fff" stroke-width="1.8"/></svg>
        </button>
      </form>
    </div>
  </header>

  <nav class="main-nav">
    <ul>
      <li class="active">Home</li>
      <li>About Paddora</li>
      <li>Classified</li>
      <li>Horses</li>
      <li>Directory</li>
      <li>Calendar</li>
      <li>Horse Pictures</li>
      <li>Forum</li>
      <li>Left</li>
      <li>Our Partners</li>
      <li>Contact</li>
    </ul>
  </nav>

  <section class="banner banner-main" role="img" aria-label="Banner photo: a young woman with a bay horse outdoors">
    <div class="banner-caption">Lorem ipsum dolor sit amet, consectetur adipiscing elit</div>
  </section>
  <a class="slide-arrow prev" aria-label="Previous">
    <svg width="14" height="24" viewBox="0 0 14 24"><path d="M12 2 L2 12 L12 22" stroke="#fff" stroke-width="1.6" fill="none"/></svg>
  </a>
  <a class="slide-arrow next" aria-label="Next">
    <svg width="14" height="24" viewBox="0 0 14 24"><path d="M2 2 L12 12 L2 22" stroke="#fff" stroke-width="1.6" fill="none"/></svg>
  </a>
  <section class="banner banner-side" role="img" aria-label="Banner photo: a rider in a red cap beside a chestnut horse in a stable">
    <div class="banner-caption">Lorem ipsum dolor sit amet</div>
  </section>

  <p class="intro">Paddora se veut un site neutre ou tous las amis das chevaux sont les blenvenus, peu importe leur niveau ou leur disciplines de predilection....</p>

  <section class="content-band">
    <div class="tiles">
      <a class="tile t-news" role="img" aria-label="Photo: a woman in a cowboy hat leading a grey horse"><span class="tile-caption">News &amp; Articles</span></a>
      <a class="tile t-ads" role="img" aria-label="Photo: two horses in a paddock"><span class="tile-caption">Petites Annonces</span></a>
      <a class="tile t-agenda" role="img" aria-label="Image: tooled leather with a horse head"><span class="tile-caption">Agenda</span></a>
      <a class="tile t-directory" role="img" aria-label="Photo: a row of bay horses over a fence"><span class="tile-caption">Annuaire</span></a>
      <a class="tile t-forum" role="img" aria-label="Photo: a white horse galloping"><span class="tile-caption">Forum</span></a>
    </div>

    <h2 class="partners-title">Our Major Partners</h2>
    <span class="partner-arrow prev" aria-label="Previous partners">
      <svg width="8" height="10" viewBox="0 0 8 10"><path d="M6 1 L2 5 L6 9" stroke="#333" stroke-width="1.8" fill="none"/></svg>
    </span>
    <div class="partners">
      <div class="partner"><span class="pb-1"></span></div>
      <div class="partner"><span class="pb-2"></span></div>
      <div class="partner"><span class="pb-3"></span></div>
      <div class="partner"><span class="pb-4"></span></div>
      <div class="partner"><span class="pb-5"></span></div>
    </div>
    <span class="partner-arrow next" aria-label="Next partners">
      <svg width="8" height="10" viewBox="0 0 8 10"><path d="M2 1 L6 5 L2 9" stroke="#333" stroke-width="1.8" fill="none"/></svg>
    </span>
  </section>

  <footer class="site-footer">Copyright 2016 Paddora. All Rights Reserved.</footer>
</body>
</html>
```